Salmon Shop that sells both wholesale and retail salmon in a variety of ways.

"Tidewater Fishery" is a business that is selling atlantic salmon in every way possible. We will be a salmon butcher to the public for retail purchase and we will also be out and about trying to sell our products to restaurants cafes and any other wholesale way. Our product is from Tasmania but we will be trading on the Sunshine Coast. The shop design has an urban, rustic feel and very much about the product. One of the owners has worked on salmon farms for 15 years and we want it to be very specialised and quality. I have nothing to offer you to help with this design....I would like both a salmon on the card, not sure if image or silohette is best and would like the other side to have a fillet with a tag of some sort. We are looking for a logo also. Use a photo of an Atlantic Salmon, Atlantic Salmon have two fins along the back.
Updates

Project Deadline Extended Reason: I am extending the deadline as I have still not got exactly what I want. All designers have added something great to what I am after and I just need someone to pull it all together. I have put in a new brief with a sketched image to help so we can get this perfect. Please read all the instructions. Thank you Added Monday, February 16, 2015

Target Market(s)

Restaurants, cafes

Industry/Entity Type

Retail

Contact Information for Business Card

Tidewater Fishery (Not to have "Shop" at the end.Shop 12/130-164 Brisbane RdMooloolaba 4557

Colors
1c66ab

Requirements
Must have
• logo for Tidewater Fishery with the S being salmon fillet of fresh salmon on white platemap of tasmaniasepia /black and white image of atlantic salmon
Nice to have
• fillet of salmonmap of tasmaniasalmon
Should not have
• Not Shop at the end.

```html
<!DOCTYPE html>
<html lang="en">
<head>
<meta charset="utf-8">
<title>Tidewater Fishery – Business Card</title>
<link rel="stylesheet" href="https://fonts.googleapis.com/css2?family=Oswald:wght@400&family=Roboto+Condensed:wght@400;700&display=swap">
<style>
  :root {
    --salmon: #f3896b;
    --paper: #ffffff;
    --ink: #1d1d1d;
    --backdrop: #ece9e4;
    --card-shadow: rgba(60, 40, 30, 0.18);
  }
  * { margin: 0; padding: 0; box-sizing: border-box; }
  html, body {
    width: 1200px;
    height: 1200px;
    overflow: hidden;
    background: var(--backdrop);
  }
  .canvas {
    position: relative;
    width: 1200px;
    height: 1200px;
  }
  .card {
    position: absolute;
    left: 190px;
    width: 820px;
    height: 460px;
    overflow: hidden;
    box-shadow: 0 10px 30px var(--card-shadow);
  }
  .card--back { top: 110px; background: var(--paper); display: flex; }
  .card--front { top: 630px; background: var(--salmon); }

  .card__panel {
    width: 40%;
    height: 100%;
    background: var(--salmon);
    display: flex;
    align-items: center;
    justify-content: center;
  }
  .card__details {
    flex: 1;
    padding: 0 0 0 50px;
    display: flex;
    align-items: center;
  }

  .brand {
    display: flex;
    align-items: center;
    gap: 16px;
    color: var(--paper);
    font-family: "Oswald", sans-serif;
    font-weight: 400;
    text-transform: uppercase;
    line-height: 1.05;
    letter-spacing: 0.04em;
  }
  .brand__mark {
    width: 18px;
    height: 18px;
    background: var(--paper);
    flex: none;
  }
  .brand__name { font-size: 34px; }
  .brand--large .brand__name { font-size: 46px; }
  .brand--large .brand__mark { width: 24px; height: 24px; }

  .card--front .brand {
    position: absolute;
    left: 390px;
    top: 120px;
  }

  .address {
    display: flex;
    gap: 8px;
    font-family: "Roboto Condensed", sans-serif;
    color: var(--ink);
    font-size: 19px;
    line-height: 1.3;
    text-transform: uppercase;
  }
  .address__icon { width: 14px; height: 20px; flex: none; margin-top: 1px; }
  .address__label { font-weight: 700; }
  .address__lines { font-weight: 400; }
</style>
</head>
<body>
  <main class="canvas">
    <section class="card card--back" aria-label="Business card, back">
      <div class="card__panel">
        <div class="brand">
          <span class="brand__mark"></span>
          <span class="brand__name">Tidewater<br>Fishery</span>
        </div>
      </div>
      <div class="card__details">
        <div class="address">
          <svg class="address__icon" viewBox="0 0 14 20" aria-hidden="true">
            <path d="M7 0C3.1 0 0 3.1 0 7c0 5 7 13 7 13s7-8 7-13c0-3.9-3.1-7-7-7zm0 9.6A2.6 2.6 0 1 1 7 4.4a2.6 2.6 0 0 1 0 5.2z" fill="currentColor"/>
          </svg>
          <div>
            <div class="address__label">Shop:</div>
            <div class="address__lines">7/210-238 Kellaway Rd.<br>Coralbay 4570</div>
          </div>
        </div>
      </div>
    </section>

    <section class="card card--front" aria-label="Business card, front">
      <div class="brand brand--large">
        <span class="brand__mark"></span>
        <span class="brand__name">Tidewater<br>Fishery</span>
      </div>
    </section>
  </main>
</body>
</html>
```